VelmaraStitch.com will be an online bespoke garment creator, specifically around designing your own Wedding Dress. It will enable you to specify your own material, colours and patterns and customized features such as bows, sequins, diamantes, and more from a selection of per-defined base garments and customize them to your taste.
The concept is similar to:
www.theorvandlane.example
But the design should reflect more like
www.quillbarn.example
www.dunwel.example - (in particular the build elements)
www.tarvo.example
It will be aimed at the Female marketplace. However this does not mean to use pink or portray the brand in very girly way. It should use good white space, and look very classy. not too busy, but functional and elegant, with a focus on stable and responsible site that will deliver. A wedding dress is an important purchase and to trust a company to make one for you from a distance takes a lot of trust from the customer perspective.
We want to first create the homepage and "build the dress" pages, which will consist of Enter your Measurements, Choose a Base Silhouette Style, Choose Fabric, Choose Colors, Customize Dress, Summary, Order Page, Thank you Page.
It will then have generic About us, How to Measure, Agent Locator, How it works, Contact, Order Samples, Support.
A very basic wire frame was created here to aid development, but the branding is being developed, so do not use any of it for inspiration just a visual interpretation - http://pexlarnode.example/velmara/
The link above is merely an idea on what areas the site will have. The actual design and colour scheme should reflect these sites.
The branding is also here - www.velmarastitch.example not the one used within that link.
The site will enable you to log in, save your designs and your delivery and measurement information. It will also offer the usual social media buttons to share the design and ability to leave comments.
This will be the first draft and the winning design will get to design the other pages and future work associated to the site.
thanks!

```html
<!DOCTYPE html>
<html lang="en">
<head>
<meta charset="utf-8">
<title>VelmaraStitch — Homepage</title>
<link href="https://fonts.googleapis.com/css2?family=Arimo:wght@400;700&display=swap" rel="stylesheet">
<style>
:root{
  --ink:#222;
  --dark:#2b2b2b;
  --band:#3a3a3a;
  --footer:#3b3b3b;
  --paper:#f4f4f4;
  --card:#ffffff;
  --line:#dcdcdc;
  --pink:#ec1c79;
  --muted:#666;
}
*{box-sizing:border-box;margin:0;padding:0}
html,body{width:993px;height:1200px;overflow:hidden}
body{position:relative;background:var(--paper);font-family:"Arimo",Arial,sans-serif;color:var(--ink);font-size:8px}
.abs{position:absolute}

/* top utility bar */
.utility-bar{left:0;top:0;width:993px;height:28px;background:var(--dark)}
.zigzag-down{left:0;top:28px;width:993px;height:5px;
  background:linear-gradient(135deg,var(--dark) 50%,transparent 50%) 0 0/5px 5px repeat-x,
             linear-gradient(225deg,var(--dark) 50%,transparent 50%) 0 0/5px 5px repeat-x}
.phone{left:179px;top:6px;display:flex;align-items:center;gap:6px;color:#fff;font-size:14px}
.phone-badge{width:17px;height:17px;background:var(--pink);border-radius:3px;display:flex;align-items:center;justify-content:center}
.utility-links{right:193px;top:9px;display:flex;gap:13px;color:#fff;font-size:8px}

/* header */
.brand{left:180px;top:43px;display:flex;align-items:center;gap:12px}
.brand-mark{width:78px;height:78px;border-radius:50%;background:#1b1b1b}
.brand-name{font-size:15px;letter-spacing:4px;color:#111}
.social{top:48px;width:32px;height:32px;border-radius:50%;background:radial-gradient(circle at 40% 35%,#4a4a4a,#1e1e1e 70%);box-shadow:0 1px 2px rgba(0,0,0,.35)}
.search{left:622px;top:104px;width:178px;height:18px;border:1px solid #bbb;border-radius:3px;background:linear-gradient(#9a9a9a,#b9b9b9);display:flex}
.search span{flex:1;color:#eee;font-size:7px;padding:4px 5px}
.search i{width:24px;background:#fff;border-left:1px solid #bbb;border-radius:0 3px 3px 0;display:flex;align-items:center;justify-content:center}

/* navigation */
.nav-band{left:0;top:134px;width:993px;height:32px;background:repeating-linear-gradient(90deg,#3c3c3c 0 2px,#333 2px 4px)}
.nav{left:178px;top:134px;width:623px;height:37px;background:var(--dark);box-shadow:0 3px 4px rgba(0,0,0,.35);display:flex;align-items:center;padding-left:19px}
.nav a{color:#fff;text-decoration:none;font-size:9.5px;padding:0 12.5px;height:37px;display:flex;align-items:center}
.nav a.is-active{background:var(--pink);font-weight:700;padding:0 13px}

/* hero */
.hero{left:178px;top:190px;width:623px;height:259px;background:var(--dark);padding:6px;box-shadow:0 8px 8px -4px rgba(0,0,0,.4)}
.hero-photo{width:100%;height:100%;background:linear-gradient(100deg,#5f6248 0%,#a89a7e 10%,#dcc8ad 24%,#ece3d6 40%,#f3efea 58%,#fafafa 100%);box-shadow:inset 0 0 30px rgba(0,0,0,.12)}
.hero-title{left:513px;top:266px;background:var(--dark);color:#fff;font-weight:700;font-size:14.5px;padding:3px 5px}
.hero-sub{left:571px;top:293px;width:190px;text-align:center;font-size:8px;line-height:1.35;color:#222}
.hero-cta{left:591px;top:320px;width:150px;height:35px;background:linear-gradient(#666,#333);color:#fff;font-weight:700;font-size:14px;display:flex;align-items:center;justify-content:center;box-shadow:0 2px 3px rgba(0,0,0,.4)}
.dots{left:739px;top:427px;display:flex;gap:2px}
.dots b{width:10px;height:10px;background:#ddd}
.dots b:first-child{background:#333}

.divider{left:178px;width:623px;height:8px;background:repeating-linear-gradient(0deg,#333 0 2px,#555 2px 3px)}

/* feature cards */
.card{top:498px;width:200px;height:157px;background:var(--card);border:1px solid var(--line);padding:6px}
.card-photo{width:100%;height:93px;box-shadow:inset 0 0 14px rgba(0,0,0,.12)}
.card h3{font-weight:400;font-size:11.5px;margin-top:5px}
.card p{width:115px;font-size:7px;line-height:1.3;color:#333;margin-top:2px}
.pill{right:7px;top:116px;width:70px;height:24px;border-radius:12px;border:2px solid #ccc;background:linear-gradient(#fff,#ddd);font-weight:700;font-size:7.5px;color:#444;display:flex;align-items:center;justify-content:center}

/* feature story */
.story{left:178px;top:690px;width:411px;height:277px;background:var(--card);border:1px solid var(--line);padding:6px}
.story-photo{width:100%;height:152px;background:radial-gradient(ellipse 70% 60% at 52% 62%,#f0eff4 0%,#cfccd8 30%,#8f8a92 55%,#4a3b2e 80%,#2e241b 100%)}
.story h2{font-size:14.5px;margin-top:6px;letter-spacing:.2px}
.story p{font-size:7px;line-height:1.65;margin-top:6px;color:#222}
.build-cta{left:203px;top:220px;width:203px;height:42px;border:1px solid #ccc;border-radius:3px;background:linear-gradient(#fff,#eee);box-shadow:0 2px 3px rgba(0,0,0,.2);color:var(--pink);font-weight:700;font-size:13px;display:flex;align-items:center;justify-content:center}

/* testimonials */
.testimonials{left:599px;top:690px;width:201px;height:200px;background:var(--card);border:1px solid var(--line)}
.panel-head{height:32px;background:repeating-linear-gradient(45deg,#3a3a3a 0 2px,#2f2f2f 2px 4px);color:#fff;font-weight:700;font-size:14.5px;display:flex;align-items:center;justify-content:center}
.avatar{left:22px;top:40px;width:53px;height:60px;background:#333;padding:5px}
.avatar div{width:100%;height:100%;background:linear-gradient(160deg,#d8b48a,#a67a52 55%,#5b7a3e)}
.client{left:93px;top:55px}
.client b{display:block;font-weight:400;font-size:11px}
.client span{font-size:7px}
.quote{left:21px;top:108px;width:160px;font-size:7px;line-height:1.65;text-align:justify}
.arrows{left:150px;top:181px;display:flex;gap:3px}
.arrows i{width:11px;height:11px;border-radius:50%;background:#444;color:#fff;font-style:normal;font-size:7px;display:flex;align-items:center;justify-content:center}
.arrows i:first-child{background:#999}

.hours{left:599px;top:901px;width:201px;height:65px;background:var(--band);color:#fff;box-shadow:0 2px 3px rgba(0,0,0,.3)}
.hours h4{left:97px;top:6px;font-weight:400;font-size:11.5px}
.hours table{left:83px;top:24px;font-size:7px;border-collapse:collapse}
.hours td{padding:1px 0}
.hours td+td{padding-left:30px;text-align:right}

/* footer */
.footer{left:0;top:991px;width:993px;height:209px;background:var(--footer);color:#fff}
.zigzag-up{left:0;top:986px;width:993px;height:5px;
  background:linear-gradient(45deg,var(--footer) 50%,transparent 50%) 0 0/5px 5px repeat-x,
             linear-gradient(-45deg,var(--footer) 50%,transparent 50%) 0 0/5px 5px repeat-x}
.foot-col{top:22px}
.foot-col h5{font-weight:400;font-size:12px;margin-bottom:6px}
.foot-col li{list-style:none;font-size:7.5px;line-height:11.6px}
.field{left:638px;width:162px;background:#fff;color:#333;font-size:7px;padding:5px 4px;border-radius:2px}
.submit{left:638px;top:182px;width:68px;height:19px;background:linear-gradient(#fff,#ddd);color:#333;font-size:7.5px;display:flex;align-items:center;justify-content:center;border-radius:2px}
.payments{left:184px;top:144px;display:flex;gap:1px}
.payments b{width:33px;height:20px;border:1px solid #888;border-radius:2px}
.foot-links{left:184px;top:177px;font-size:7.5px}
.copyright{left:184px;top:192px;font-size:7.5px}
</style>
</head>
<body>

<div class="abs utility-bar"></div>
<div class="abs zigzag-down"></div>
<div class="abs phone">
  <span class="phone-badge"><svg width="10" height="10" viewBox="0 0 10 10"><path d="M2 1 L3.5 1 L4 3 L3 3.8 C3.6 5.2 4.8 6.4 6.2 7 L7 6 L9 6.5 L9 8 C9 8.6 8.5 9 8 9 C4.5 9 1 5.5 1 2 C1 1.5 1.4 1 2 1Z" fill="#fff"/></svg></span>
  1800 -555-0142
</div>
<div class="abs utility-links"><span>My Account</span><span>Manage Order</span><span>Order status</span><span>Login</span></div>

<div class="abs brand">
  <div class="brand-mark"></div>
  <span class="brand-name">VELMARASTITCH</span>
</div>

<div class="abs social" style="left:652px" role="img" aria-label="Social network link"></div>
<div class="abs social" style="left:691px" role="img" aria-label="Social network link"></div>
<div class="abs social" style="left:729px" role="img" aria-label="Social network link"></div>
<div class="abs social" style="left:768px" role="img" aria-label="Social network link"></div>

<div class="abs search"><span>Search</span><i><svg width="11" height="11" viewBox="0 0 11 11"><circle cx="4.5" cy="4.5" r="3.3" fill="none" stroke="#777" stroke-width="1.2"/><path d="M7 7 L10 10" stroke="#777" stroke-width="1.5"/></svg></i></div>

<div class="abs nav-band"></div>
<nav class="abs nav">
  <a class="is-active">Home</a><a>About us</a><a>Build the dress</a><a>Agent Locator</a><a>How it works</a><a>Order samples</a><a>Support</a><a>Contact</a>
</nav>

<section class="abs hero">
  <div class="hero-photo" role="img" aria-label="Photograph of a bride in a lace gown with a flower crown, in soft morning light"></div>
</section>
<div class="abs hero-title">Choose Colours, Fabrics and Styles</div>
<p class="abs hero-sub">Create and order your own bespoke online gown with just few easy steps</p>
<div class="abs hero-cta">Get Started</div>
<div class="abs dots"><b></b><b></b><b></b><b></b></div>

<div class="abs divider" style="top:478px"></div>

<article class="abs card" style="left:178px">
  <div class="card-photo" role="img" aria-label="Photograph of fabric rolls, scissors and thread" style="background:linear-gradient(120deg,#9c1a22 0%,#e8d33a 22%,#f2e35a 38%,#b5202c 60%,#e9dfd8 80%,#f4f1ee 100%)"></div>
  <h3>Create Your Own</h3>
  <p>Create your own fabulous design gown with selecting create now button.</p>
  <div class="abs pill">Create Now</div>
</article>
<article class="abs card" style="left:389px">
  <div class="card-photo" role="img" aria-label="Photograph of a dressmaker measuring fabric on a table" style="background:linear-gradient(180deg,#ece9e4 0%,#d9d4cc 35%,#8e877e 55%,#cfcac3 75%,#a39c92 100%)"></div>
  <h3>Measure Yourself</h3>
  <p>Measure your made to fit design gown by selecting measure now button.</p>
  <div class="abs pill">Measure Now</div>
</article>
<article class="abs card" style="left:600px">
  <div class="card-photo" role="img" aria-label="Illustration of a street map under a magnifying glass with a location pin" style="background:linear-gradient(135deg,#eee6b4 0%,#cfe1a8 30%,#e9e4c9 50%,#a9cfe0 75%,#d7e6b0 100%)"></div>
  <h3>Agent Locator</h3>
  <p>Find agent in your area and book appointment by selecting Find Agent button.</p>
  <div class="abs pill">Find Agent</div>
</article>

<div class="abs divider" style="top:669px"></div>

<article class="abs story">
  <div class="story-photo" role="img" aria-label="Photograph of a white satin wedding gown with a long train"></div>
  <h2>Custom Wedding Dress From VelmaraStitch</h2>
  <p>Lorem Ipsum dolor sit amet consitectur. Proin gravida nibh vel velit auctor aliquet. Aenean sollicitudin, lorem quis bibendum auctor, nisi elit consequat ipsum, nec sagittis sem nibh id elit. Duis sed odio sit amet nibh vulputate cursus a sit amet mauris.</p>
  <div class="abs build-cta">Build Your Dress NOW</div>
</article>

<aside class="abs testimonials">
  <div class="panel-head">Testimonials</div>
  <div class="abs avatar"><div role="img" aria-label="Portrait photo of the customer"></div></div>
  <div class="abs client"><b>Corra Wendle</b><span>London, United Kingdom</span></div>
  <p class="abs quote">Sed non neque elit. Sed ut imperdiet nisi. Proin condimentum fermentum nunc. Etiam pharetra, erat sed fermentum feugiat, velit mauris egestas quam, ut aliquam massa nisl quis neque. Suspendisse in orci enim.</p>
  <div class="abs arrows"><i>‹</i><i>›</i></div>
</aside>

<aside class="abs hours">
  <svg class="abs" style="left:12px;top:9px" width="48" height="48" viewBox="0 0 48 48"><circle cx="24" cy="24" r="21" fill="none" stroke="#fff" stroke-width="3"/><path d="M24 11 V25 L17 31" fill="none" stroke="#fff" stroke-width="3"/></svg>
  <h4 class="abs">Opening Time</h4>
  <table class="abs">
    <tr><td>Mon - Fri</td><td>8:00 to 18:00</td></tr>
    <tr><td>Sat:</td><td>9:00 to 18:00</td></tr>
    <tr><td>Sun:</td><td>10:00 to 16:00</td></tr>
  </table>
</aside>

<div class="abs zigzag-up"></div>
<footer class="abs footer">
  <div class="abs foot-col" style="left:184px"><h5>About us</h5><ul><li>Home</li><li>About us</li><li>Testimonials</li><li>Contact us</li><li>Sitemap</li></ul></div>
  <div class="abs foot-col" style="left:281px"><h5>Information</h5><ul><li>Blog</li><li>FAQs</li><li>News</li><li>Terms &amp; Conditions</li><li>Privacy Policy</li></ul></div>
  <div class="abs foot-col" style="left:378px"><h5>My Account</h5><ul><li>Manage Order</li><li>Order History</li><li>Order Status</li><li>Shipping Status</li><li>Help Support</li></ul></div>
  <div class="abs foot-col" style="left:489px"><h5>Product</h5><ul><li>Overview</li><li>Gown Styles</li><li>Agent Locator</li><li>Measure Yourself</li><li>Style Guide</li></ul></div>
  <div class="abs foot-col" style="left:638px"><h5>Feedback</h5></div>
  <div class="abs field" style="top:45px;height:19px">Name</div>
  <div class="abs field" style="top:72px;height:19px">Email</div>
  <div class="abs field" style="top:98px;height:78px">Message</div>
  <div class="abs submit">Submit</div>
  <div class="abs payments" role="img" aria-label="Accepted payment methods">
    <b style="background:#e8a33a"></b><b style="background:#2f6fb8"></b><b style="background:#6fa7d8"></b><b style="background:#f2f2f2"></b><b style="background:#f6efe2"></b><b style="background:#f3ead0"></b>
  </div>
  <div class="abs foot-links">Site Map &nbsp;| &nbsp;Search Terms &nbsp;| &nbsp;Advanced Search &nbsp;| &nbsp;Order and Returns &nbsp;| &nbsp;Contact us</div>
  <div class="abs copyright">2012 VelmaraStitch Ltd. All Rights Reserved.</div>
</footer>

</body>
</html>
```